Healthcare Consulting company business card

We are looking for a business card design for a new healthcare consulting company. The company is looking to provide assistance to large healthcare organisations in the following categories:
Acute care and critical care
Tender documents and applications
CV, job applications and interview skills
scientific lecture presentation preparations and skills
research and quality activities
medical equipment and device consulting
hemofiltration liaising.
Please see the attached file below for the design brief.
Alternative designs are welcomed.
Business
Contact Information for Business Card
Name: Rex Tulloch
Mobile: 0427 816 094
Email: rextullochconsulting@mailbox-example.com
Website: www.rextullochconsulting-example.com.au

```html
<!DOCTYPE html>
<html lang="en">
<head>
<meta charset="utf-8">
<title>Rex Tulloch Consulting – Business Card</title>
<link rel="stylesheet" href="https://fonts.googleapis.com/css2?family=Arimo:wght@400&display=swap">
<style>
  :root {
    --brand-blue: #0c56a6;
    --tile-blue-soft: #2a6cb5;
    --card-white: #ffffff;
    --stage: #e9e6e1;
  }
  * { box-sizing: border-box; margin: 0; padding: 0; }
  html, body { width: 1200px; height: 1200px; overflow: hidden; }
  body {
    background: var(--stage);
    font-family: "Arimo", Arial, sans-serif;
    position: relative;
  }
  .card {
    position: absolute;
    left: 256px;
    width: 700px;
    height: 400px;
    box-shadow: 0 18px 30px rgba(0,0,0,0.18);
  }
  .card--front { top: 110px; background: var(--card-white); color: var(--brand-blue); }
  .card--back  { top: 666px; background: var(--brand-blue); color: var(--card-white); }

  .wordmark {
    position: absolute;
    font-weight: 400;
    white-space: nowrap;
    line-height: 1;
  }
  .card--front .wordmark { left: 336px; top: 92px; font-size: 31px; }
  .card--back .wordmark  { left: 0; right: 0; text-align: center; top: 126px; font-size: 38px; }

  .contact {
    position: absolute;
    left: 33px;
    top: 171px;
    list-style: none;
    font-size: 17.5px;
    line-height: 23.5px;
  }

  .services {
    position: absolute;
    left: 33px;
    top: 287px;
    display: flex;
    gap: 66px;
  }
  .service-tile {
    width: 74px;
    height: 72px;
    border-radius: 7px;
    background: var(--brand-blue);
  }
  .card--back .services { left: 31px; top: 286px; gap: 64px; }
  .card--back .service-tile {
    width: 76px;
    height: 75px;
    border: 2px solid var(--card-white);
    background: var(--tile-blue-soft);
  }
</style>
</head>
<body>
  <section class="card card--front">
    <div class="wordmark">Rex Tulloch Consulting</div>
    <ul class="contact">
      <li>Name: Rex Tulloch</li>
      <li>Mobile: 0427 816 094</li>
      <li>Email: rextullochconsulting@mailbox-example.com</li>
      <li>Website: www.rextullochconsulting-example.com.au</li>
    </ul>
    <div class="services">
      <div class="service-tile" role="img" aria-label="Icon: consultant presenting tender and funding advice"></div>
      <div class="service-tile" role="img" aria-label="Icon: heart with heartbeat line for acute and critical care"></div>
      <div class="service-tile" role="img" aria-label="Icon: two people in an interview conversation"></div>
      <div class="service-tile" role="img" aria-label="Icon: presenter addressing an audience"></div>
      <div class="service-tile" role="img" aria-label="Icon: test tubes and microscope for research"></div>
    </div>
  </section>

  <section class="card card--back">
    <div class="wordmark">Rex Tulloch Consulting</div>
    <div class="services">
      <div class="service-tile" role="img" aria-label="Icon: consultant presenting tender and funding advice"></div>
      <div class="service-tile" role="img" aria-label="Icon: heart with heartbeat line for acute and critical care"></div>
      <div class="service-tile" role="img" aria-label="Icon: two people in an interview conversation"></div>
      <div class="service-tile" role="img" aria-label="Icon: presenter addressing an audience"></div>
      <div class="service-tile" role="img" aria-label="Icon: test tubes and microscope for research"></div>
    </div>
  </section>
</body>
</html>
```